Premium Nail Dip Powder Label Design

We need a label design for a 2 ounce jar in which we will be selling our new product line of dip powder to nail salons. For reference, please see competitors' products that are currently selling in the market. The label size is 16cm long by 2.5cm wide. We have a logo design that is attached - the "drop" should be in shiny gold (metallic). This label will wrap around the round jar and the first half will be the "front" and the second half will be the "back". Please see the attached writing that will be required for the second half, or "back" part of the label.

Target Market(s)

Retail Nail Salons in the US

Font styles to use
Sans Serif

Colors

Designer to choose colors to be used in the design.

Requirements
Must have
• "RWT" logo with the "drop" in shiny/metallic gold to match the shiny gold lid that we will have for it. The words "Premium Dip Powder". The size "2 oz". The wording for the second half, or "back" part of the label attached should be in black color with the size adjusted to fit the label size.
Nice to have
• different designs of fonts and sizes and colors for "Premium Dip Powder" which should be on the "front" of the label under our logo.

```html
<!DOCTYPE html>
<html lang="en">
<head>
<meta charset="utf-8">
<title>Premium Dip Powder – Jar Label</title>
<link href="https://fonts.googleapis.com/css2?family=Poppins:wght@200;600;800&family=Questrial&family=Raleway:wght@700&family=Roboto+Condensed:wght@300;700&display=swap" rel="stylesheet">
<style>
  :root{
    --plum:#2a0514;
    --plum-light:#4a2a36;
    --white:#ffffff;
    --gold:#e2ad22;
  }
  html,body{margin:0;padding:0;width:1200px;height:1200px;overflow:hidden;background:var(--plum);}
  .label{display:block;width:1200px;height:1200px;}
  .premium{font-family:'Poppins',sans-serif;font-weight:200;font-size:50px;fill:var(--white);}
  .dip{font-family:'Poppins',sans-serif;font-weight:800;font-size:74px;fill:var(--white);letter-spacing:-2px;}
  .powder{font-family:'Poppins',sans-serif;font-weight:600;font-size:22px;fill:var(--white);}
  .brand-name{font-family:'Poppins',sans-serif;font-weight:800;font-size:46px;fill:var(--gold);}
  .brand-dot{fill:var(--gold);}
  .size{font-family:'Questrial',sans-serif;font-size:15px;fill:var(--white);}
  .side-small{font-family:'Roboto Condensed',sans-serif;font-weight:300;font-size:11.5px;fill:var(--white);}
  .side-bold{font-family:'Roboto Condensed',sans-serif;font-weight:700;font-size:12px;fill:var(--white);}
  .heading{font-family:'Raleway',sans-serif;font-weight:700;font-size:15.5px;fill:var(--white);}
  .body{font-family:'Questrial',sans-serif;font-size:15.5px;fill:var(--white);}
  .caution{font-family:'Raleway',sans-serif;font-weight:700;font-size:13px;fill:var(--white);}
  .fine{font-family:'Questrial',sans-serif;font-size:12.6px;fill:var(--white);}
</style>
</head>
<body>
<svg class="label" viewBox="0 0 1200 1200" xmlns="http://www.w3.org/2000/svg">
  <defs>
    <linearGradient id="size-band" x1="0" y1="0" x2="0" y2="1">
      <stop offset="0" stop-color="#4a2a36" stop-opacity="0.9"/>
      <stop offset="1" stop-color="#4a2a36" stop-opacity="0.2"/>
    </linearGradient>
  </defs>

  <!-- Front panel -->
  <g class="front-panel">
    <text class="premium" transform="translate(209 690) rotate(-90)">Premium</text>
    <text class="dip" x="216" y="594">DIP</text>
    <text class="powder" x="220" y="620">Powder</text>

    <rect class="size-band" x="458" y="520" width="40" height="176" fill="url(#size-band)"/>

    <g class="brand-mark">
      <circle class="brand-dot" cx="330" cy="650" r="9"/>
      <text class="brand-name" x="348" y="666">RWT</text>
    </g>

    <text class="size" x="461" y="693">2 .oz</text>
  </g>

  <!-- Back panel -->
  <g class="back-panel">
    <text class="side-small" transform="translate(677 665) rotate(-90)">Manufactured Exclusively For</text>
    <text class="side-bold" transform="translate(692 676) rotate(-90)">Bluewater Trading, Inc., USA</text>
    <text class="side-small" transform="translate(708 664) rotate(-90)">www.bluewatertrading.com</text>

    <g text-anchor="end">
      <text class="heading" x="1030" y="535">FOR USE BY NAIL PROFESSIONALS ONLY</text>
      <text class="body" x="1030" y="553">INGREDIENTS:  Polyethylmethacrylate,</text>
      <text class="body" x="1030" y="572">Acrylates Copolymer, Benzoyl Peroxide</text>
      <text class="body" x="1030" y="591">and PEG-12 Dimethicone. May also contain</text>
      <text class="body" x="1030" y="610">various coloring agents and glitters.</text>
      <text class="caution" x="1027" y="634">CAUTION</text>
      <text class="fine" x="1027" y="647">KEEP OUT OF REACH OF CHILDREN.</text>
      <text class="fine" x="1027" y="661">Keep away from heat, humidity and sunlight</text>
      <text class="fine" x="1027" y="674">Discontinue use if sensitivityor irritation occurs.</text>
    </g>
  </g>
</svg>
</body>
</html>
```